Say goodbye to Paper Cuts - Modern B2B Paper Ad

We need a design for a full page magazine ad

Company Overview:
FileNimbus is an administration support company for Northern Lending Insider. We are running a full page ad in Northern Lending Insider magazine

Ad Copy
"Say Goodbye to Paper Cuts"
"On-Demand Admin Support for Mortgage Professionals"
[website url at the bottom]

Ad Dimensions:
Trim: (w) 8.25” x (h) 10.875”
Bleed: (w) 8.75” x (h) 11.375”
Type: (w) 7.5” x (h) 10.125”

Ad Requirements (provided by the magazine)
Please supply all artwork in PC format only, either in EPS, Tiff or PDF format with the following requirements:

- All files must be 300 dpi high resolution with CMYK process colour.
- Any Pantone colours that are found will automatically be converted to CMYK. Please double check that all colours are in CMYK.
- EPS files must be in outline path for all fonts and embedded images.
- Tiff files must be in PC format, flatten with no layer.
- PDF files must be press optimized and embedded with images and fonts.
- All Double page ads and Full page ads must be in press-optimized PDF files.
- 0.125" bleed with crop marks are required for Double page ads, Full page ads and Panel ads to be supplied on artwork where specified.
- Ad files in Microsoft Word, Excel, PowerPoint or other software are NOT acceptable.
- Materials received should be in a printable file with no conversion required.

Industry/Entity Type

It Company

Font styles to use
Sans Serif

Requirements
Must have
• Bold, clean style

```html
<!DOCTYPE html>
<html lang="en">
<head>
<meta charset="utf-8">
<title>FileNimbus – Say Goodbye to Paper Cuts</title>
<link href="https://fonts.googleapis.com/css2?family=Roboto+Condensed:ital,wght@0,400;0,700;0,900;1,700&family=Roboto:wght@400;700;900&display=swap" rel="stylesheet">
<style>
  :root {
    --brand-blue: #1d4f9c;
    --brand-navy: #1b2d58;
    --ink-grey: #4a5668;
    --paper: #f4f6f9;
    --paper-shade: #dfe4eb;
    --photo-deep: #1f2733;
    --photo-mid: #5a6678;
    --photo-light: #c9d0da;
    --glow: #7fd6ff;
  }
  html, body {
    margin: 0;
    width: 959px;
    height: 1200px;
    overflow: hidden;
    background: #ffffff;
  }
  .ad-page {
    position: relative;
    width: 959px;
    height: 1200px;
    overflow: hidden;
    background: linear-gradient(180deg, var(--paper) 0%, #ffffff 55%, var(--paper-shade) 100%);
    font-family: "Roboto", sans-serif;
  }
  .hero-photo {
    position: absolute;
    left: 0; top: 0;
    width: 959px;
    height: 680px;
    background:
      radial-gradient(ellipse 55% 45% at 62% 55%, rgba(230,236,244,0.9) 0%, rgba(230,236,244,0) 70%),
      linear-gradient(110deg, var(--photo-light) 0%, var(--photo-mid) 45%, var(--photo-deep) 100%);
  }
  .hero-fade {
    position: absolute;
    left: 0; top: 440px;
    width: 959px;
    height: 260px;
    background: linear-gradient(180deg, rgba(244,246,249,0) 0%, var(--paper) 100%);
  }
  .mortgage-key {
    position: absolute;
    left: 430px;
    top: 300px;
    width: 330px;
    height: 74px;
    border-radius: 8px;
    background: rgba(127,214,255,0.18);
    box-shadow: 0 0 28px rgba(127,214,255,0.85), inset 0 0 14px rgba(127,214,255,0.6);
    display: flex;
    align-items: center;
    justify-content: center;
    font-family: "Roboto Condensed", sans-serif;
    font-weight: 700;
    font-size: 52px;
    letter-spacing: 2px;
    color: #ffffff;
    text-shadow: 0 0 14px var(--glow);
  }
  .headline {
    position: absolute;
    left: 0;
    top: 640px;
    width: 959px;
    font-family: "Roboto Condensed", sans-serif;
    line-height: 1;
  }
  .headline .say {
    position: absolute;
    left: 90px;
    top: 0;
    font-weight: 900;
    font-size: 98px;
    color: var(--brand-blue);
  }
  .headline .goodbye {
    position: absolute;
    left: 86px;
    top: 92px;
    font-weight: 900;
    font-size: 214px;
    letter-spacing: -2px;
    color: var(--brand-blue);
  }
  .headline .to-paper-cuts {
    position: absolute;
    left: 520px;
    top: 302px;
    font-weight: 700;
    font-size: 58px;
    color: var(--brand-navy);
  }
  .tagline {
    position: absolute;
    left: 90px;
    top: 1012px;
    font-family: "Roboto Condensed", sans-serif;
    font-style: italic;
    font-weight: 700;
    font-size: 33px;
    color: var(--brand-blue);
  }
  .footer-bar {
    position: absolute;
    left: 90px;
    top: 1078px;
    display: flex;
    align-items: center;
    gap: 26px;
    font-family: "Roboto", sans-serif;
    color: var(--brand-navy);
  }
  .brand {
    display: flex;
    align-items: center;
    gap: 10px;
    font-weight: 900;
    font-size: 38px;
    color: var(--brand-navy);
  }
  .brand-square {
    width: 30px;
    height: 30px;
    background: var(--brand-blue);
  }
  .divider {
    width: 2px;
    height: 44px;
    background: var(--ink-grey);
  }
  .login {
    font-weight: 700;
    font-size: 28px;
    color: var(--brand-blue);
  }
  .web {
    font-weight: 700;
    font-size: 28px;
    color: var(--brand-navy);
  }
</style>
</head>
<body>
<main class="ad-page">
  <div class="hero-photo" role="img" aria-label="Businessman in a dark suit pointing a finger at a glowing on-screen button"></div>
  <div class="hero-fade"></div>
  <div class="mortgage-key">MORTGAGE</div>

  <h1 class="headline">
    <span class="say">SAY</span>
    <span class="goodbye">GOODBYE</span>
    <span class="to-paper-cuts">To Paper Cuts</span>
  </h1>

  <p class="tagline">On-Demand Admin Support for Mortgage Professionals</p>

  <footer class="footer-bar">
    <div class="brand"><span class="brand-square"></span>FileNimbus</div>
    <span class="divider"></span>
    <span class="login">LOG IN</span>
    <span class="web">www.filenimbus.ca</span>
  </footer>
</main>
</body>
</html>
```